Creating business cards for our new private medical clinic in London

Hey everyone,

We are starting a new private medical clinic in central London. We already have our logo (please see the 2 different layouts of the logo attached.) Please note that we are not restricted to using only this font in the card though.

The cards will be printed by "Pekko." The cards have a textured surface and a coloured middle layer - please see this webpage for the exact product spec (https://www.pekkoprint.example/uk/products/velvet/business-cards.html). We're overall looking for a modern yet highly professional look. We'd like the cards to have Square edges and NOT rounded please.

We need a standard card that uses one or both of our logo's colours (blue and green), and another card for premium customers, that uses black with either gold/silver/bronze. On the black coloured cads, please could you add the word "Black Account" or the word "Black" under the logo text - wherever you think it looks best?

_________________

AMENDMENT TO BRIEF:

1) The first batch of our cards are to be promotional cards and need to have more information. Could please have one card that is more like an "information card" that has the following information: - (There's a lot there and we might need to slim this down once we see the cards.)

GP appointments £70
-Feeling unwell
-Referrals to private specialists
-Sexual health check up
-Contraception
-Second opinion

Launch Offer
First appointment £40 with this card until 30 September 2017

Book online

2) Could you see whether we could add a 'strap line' to the card, something like: “Stay in Optimal Health”

_____________

The files attached have 2 versions of our logo - one linear and with the words 'stacked'; we think that the stacked logo may work better for the business card but we'd love to see different versions.

On one side of the card could we please see a coloured background, with a design containing our logo? On the other side of the card, please could we have a different coloured or white background and the information below.

Address: THE HARROWFIELD CLINIC @ FitVanta, 19 Bramblecote Lane, London, EC2Z 4QJ
Open: Mon-Fri (early & late appointments)
Book Online: www.harrowfieldclinic.example
Email: bookings@harrowfieldclinic.example
Phone number: (We don't have this yet - but please leave a space for this to go into.)

Other possible design features:

Because our clinic is located in the financial district of London, anything that represents this (e.g. The City of London's skyline - i.e. financial district - could look nice (example buildings include: The Pinecone, The Teacup-Tower, The Wedgehouse, St Aldric Minster, Keep of Brennmoor, Gantry Crossing, The Spindle). We wondered whether a outline or drawing of these buildings in the background of the card could look nice. Please see the image link below to get an idea of the skyline we're looking for:

https://img.stockvale.example/z/skyline-hand-drawn-city-pastel-shades-heritage-buildings-futuristic-81920457.jpg

The following image links are examples of cards that we've seen online and like the overall feel of (of course our colours are different):

http://www.craftnook.example/diverse/2/goodcards/73014589122.jpg
http://cardheron.example/wp-content/uploads/2013/01/cool-business-cards-saffron.jpg
https://cardfolio.example/wp-content/uploads/20461-cool-business-card-mockup.jpg
http://www.plinthworks.example/wp-content/uploads/edd/2015/08/Modern-Tutor-Business-Card-Template-Preview.jpg
http://lorvelandkit.example/wp-content/uploads/2017/01/design-a-business-card-cool-business-card-designsqx83.jpg
http://makerspindle.example/resources/files/articles/harbor-print/copper-foil-business-cards.jpg

STATIONARY:
We will also need the following stationary designed by our chosen designer. We’d like stationary to use one or both the colours of our logo (ie Green and Blue). Please use these colours to add any additional design features to stationary - other similar palette colours can also be used. Our logo font is - abeatbyKai - and this could be used in other parts of the stationary, but please feel free to try other fonts too. We prefer sans serif fonts.

Overall - we are open to all ideas but we need a look and feel that looks modern and highly professional. For our letter, prescription and medical report templates we need these to be PDFs and word processing files that can merge relevant data and text into different sections.

The information required on various pieces of stationary are as follows:

Letterheads:
These need to have:
Clinic's: Logo / Address / Phone Number / Website / Email address / Recipients address.
The letter can have address data either at the top or as a footer. We're happy to see designs that use either to see which one looks best (same goes for other pieces of stationary too.)

Invoices:
Invoice number: (Unique code for document)
Invoice Date:
Clinic’s: Logo / Address / Phone Number / Website / Email address
Services: Service Code / Name of Service / Price
Total Price:
PAYLO, Cardwise and Northern Remit Logos
Patient details: Patient’s Name / Address

Prescription Pads:
Prescription number: (Unique code for document)
Clinic details: Clinic’s Logo / Address / Phone Number / Website / Email address
Patient details needed include: Patient’s Name / Date of birth / address
Blank space required to write the name of medication
Doctors Signature: and space for signature
MPB Number: and space for this to be entered

Templates for our medical reports:
These are reports we will be printed (on good quality paper) for patients after they have had a complete health check. They will include a text summary, and the results of any tests (with graphs) and images of scans. Please could we see how text/titles/headings/tables etc could be styled?
They will need the following details: -
Clinic details needed include: Clinic’s Logo / Address / Phone Number / Website / Email address
Date of Report:
Then the following sections need to be includes:
1) Free Text Space
2) Space for images and text
3) Space for blood test and text

___________________

Thanks so much everyone.

All the best,

Tev and Dane

Target Market(s)

City of London
Private Healthcare

Industry/Entity Type

Health Care

Contact Information for Business Card

Font styles to use
Sans Serif

Colors
33a6d7
25a0d3
add136
9bcb3c
cadf82
85acd3
3276b5
0255a3
85cae6

Requirements
Must have
• Please see project description for details.
Nice to have
• Perhaps a outline/drawing/illustration of the City of London skyline (i.e. the Pinecone and surrounding buildings)

```html
<!DOCTYPE html>
<html lang="en">
<head>
<meta charset="utf-8">
<title>The Harrowfield Clinic – Business Cards</title>
<link rel="stylesheet" href="https://fonts.googleapis.com/css2?family=Open+Sans:ital,wght@0,300;0,400;0,600;0,700;1,400;1,600;1,700&display=swap">
<style>
  :root {
    --page-bg: #e6e7e9;
    --lime: #cde92e;
    --lime-deep: #b6dc1f;
    --brand-blue: #33a6d7;
    --brand-green: #9bcb3c;
    --ink: #111111;
    --text-grey: #5b5f63;
    --card-white: #ffffff;
    --rule-blue: #5fb8e0;
  }
  * { box-sizing: border-box; margin: 0; padding: 0; }
  html, body {
    width: 1200px; height: 1200px; overflow: hidden;
    background: var(--page-bg);
    font-family: "Open Sans", sans-serif;
  }
  .sheet {
    width: 1200px; height: 1200px;
    display: flex; flex-direction: column; align-items: center; justify-content: center;
    gap: 56px;
  }
  .card {
    width: 760px; height: 492px;
    position: relative;
    box-shadow: 0 6px 18px rgba(0,0,0,.12);
  }

  /* Front */
  .card--front {
    background: linear-gradient(120deg, var(--lime-deep) 0%, var(--lime) 60%, #d6f03c 100%);
    display: flex; flex-direction: column; align-items: center; justify-content: center;
    color: var(--ink);
  }
  .wordmark { display: flex; align-items: center; gap: 18px; }
  .wordmark__square { width: 44px; height: 44px; background: currentColor; }
  .wordmark__name { font-weight: 300; font-size: 52px; letter-spacing: -0.5px; line-height: 1; }
  .strapline { margin-top: 26px; font-size: 30px; font-weight: 400; letter-spacing: .5px; }

  /* Back */
  .card--back { background: var(--card-white); padding: 40px 48px 36px; color: var(--text-grey); }
  .card--back .wordmark { color: var(--brand-blue); }
  .card--back .wordmark__square { width: 38px; height: 38px; background: var(--brand-green); }
  .card--back .wordmark__name { font-size: 44px; }
  .opening {
    margin-top: 22px; color: var(--brand-blue);
    font-style: italic; font-weight: 700; font-size: 30px;
  }
  .contact-grid {
    margin-top: 14px; display: grid; grid-template-columns: 1fr 1fr;
    border-bottom: 1.5px solid var(--rule-blue); padding-bottom: 14px;
  }
  .contact-grid__col { font-size: 15px; line-height: 1.6; }
  .contact-grid__col + .contact-grid__col { border-left: 1.5px solid var(--rule-blue); padding-left: 18px; }
  .label { color: var(--brand-blue); font-weight: 600; font-size: 16px; }
  .services { margin-top: 14px; font-size: 15px; line-height: 1.6; }
  .services__title, .offer__title { color: var(--brand-blue); font-weight: 700; font-style: italic; font-size: 17px; }
  .offer { font-size: 15px; line-height: 1.7; border-bottom: 1.5px solid var(--rule-blue); padding-bottom: 8px; }
  .offer strong { color: #333; font-weight: 700; }
</style>
</head>
<body>
<main class="sheet">
  <section class="card card--front" aria-label="Card front">
    <div class="wordmark">
      <span class="wordmark__square" aria-hidden="true"></span>
      <span class="wordmark__name">The Harrowfield Clinic</span>
    </div>
    <p class="strapline">Stay In Optimal Health</p>
  </section>

  <section class="card card--back" aria-label="Card back">
    <div class="wordmark">
      <span class="wordmark__square" aria-hidden="true"></span>
      <span class="wordmark__name">The Harrowfield Clinic</span>
    </div>
    <p class="opening">Open : Monday - Friday</p>
    <div class="contact-grid">
      <div class="contact-grid__col">
        <p class="label">BOOK ONLINE</p>
        <p><span class="label">W :</span> www.harrowfieldclinic.example</p>
        <p><span class="label">E :</span> bookings@harrowfieldclinic.example</p>
      </div>
      <div class="contact-grid__col">
        <p class="label">THE HARROWFIELD CLINIC</p>
        <p>@ FitVanta</p>
        <p>19 Bramblecote Lane, London, EC2Z 4QJ</p>
      </div>
    </div>
    <div class="services">
      <p class="services__title">GP appointments £70</p>
      <p>Feeling unwell, Referrals to private specialists, Sexual health check up, Contraception, Second opinion</p>
    </div>
    <p class="offer"><span class="offer__title">Introductory Offer -</span> £30 off first appointment with this card until <strong>30 September 2017</strong></p>
  </section>
</main>
</body>
</html>
```